Brochure layout for a small country church

St. Wendel is a small country church located on the central coast of CA. Last year our priest retired, and we are in the process of seeking a new church leader. To support our search process, we created a profile brochure that describes who we are in words and images.

The copy has been carefully written and fully edited, and we have gathered, tagged and foldered high-resolution images. We now need a person with your talents to arrange the words and pictures for us!

This document, which we call a 'profile' but is actually a brochure, will be in PDF format, size 8.5x11, for web display and local printing only. It will be posted on a national database and be shared with candidates by email and on our website. We do not intend to reproduce this on paper, though we expect some users will print pages on their printers.

Here is a Cloudpail link to access the copy, images and layout instructions:
https://www.cloudpail-share.net/sh/k3rtezn7wqa8u2x/BBDQLM-17h88_pR4TUwnXoEbz

The layout instructions include specific information on image placement, and gives you much flexibility to arrange the copy/images the way you think looks best. All we ask is that you do not change the copy.

Images may be processed, cropped, inverted, enhanced … whatever you think looks right. We tried to give you the largest images possible, so you can get good resolution on the page.

Please do not let the length of the document concern you … you can cut/paste the copy, using any serif font that matches the look/feel of our church, and all of the images have been tagged and folder addressed in the document so you know where to find them. Page count does not matter as long as it looks good, and once you start laying out the pages it should not take long to finish. We just need someone with your design skills to make it look good!

As we stated in the copy narrative, we are a warm, loving and inclusive parish that is humble, happy and grateful for the many blessings we have. Our greatest quality is our people. In your design work, anything you can do to bring forward these values will be appreciated.

If you have any questions, please do not hesitate to contact me (Gordon Pelley/gordon@gordonpelley-mail.net) and I will answer them for you right away.

Thank you for considering our brochure project, and we look forward to your submission.

Industry/Entity Type

Church

```html
<!DOCTYPE html>
<html lang="en">
<head>
<meta charset="utf-8">
<title>St. Wendel Parish Profile – pages 5 and 6</title>
<link href="https://fonts.googleapis.com/css2?family=Zilla+Slab:wght@300;400;500&display=swap" rel="stylesheet">
<style>
  :root {
    --backdrop: #7f7263;
    --paper: #ffffff;
    --ink: #1f1c1a;
    --tab: #a8d3dd;
    --wood-light: #94522a;
    --wood-dark: #5e2c14;
    --church-light: #d9dcd6;
    --church-dark: #7f7a70;
    --nave-light: #efe0c6;
    --nave-dark: #5d4333;
  }
  * { box-sizing: border-box; margin: 0; padding: 0; }
  html, body { width: 1200px; height: 900px; overflow: hidden; }
  body {
    background: var(--backdrop);
    position: relative;
    font-family: "Zilla Slab", Georgia, serif;
    color: var(--ink);
    font-size: 7.7px;
    line-height: 1.33;
  }
  .page {
    position: absolute;
    top: 113px;
    width: 520px;
    height: 672px;
    background: var(--paper);
    overflow: hidden;
  }
  .page--left { left: 72px; }
  .page--right { left: 608px; }
  .photo { position: absolute; }
  .photo--crucifix { left: 24px; top: 0; width: 472px; height: 281px;
    background: linear-gradient(160deg, var(--wood-light), var(--wood-dark)); }
  .photo--doorway { left: 266px; top: 0; width: 230px; height: 200px;
    background: linear-gradient(180deg, var(--church-light) 0%, #b9b6ad 55%, var(--church-dark) 100%); }
  .photo--congregation { left: 24px; top: 347px; width: 230px; height: 325px;
    background: linear-gradient(175deg, var(--nave-light) 0%, #c7a98a 45%, var(--nave-dark) 100%); }
  h2 {
    font-weight: 300;
    font-size: 23px;
    line-height: 1;
    letter-spacing: 0.2px;
    position: absolute;
  }
  p { margin-bottom: 6px; }
  ul { list-style: none; }
  .list > li { position: relative; padding-left: 13px; margin-bottom: 2px; }
  .list > li::before { content: "•"; position: absolute; left: 2px; }
  .sublist > li { position: relative; padding-left: 10px; margin-bottom: 1px; }
  .sublist > li::before { content: "›"; position: absolute; left: 1px; }
  .qualities { position: absolute; top: 385px; left: 24px; width: 472px; display: flex; gap: 8px; }
  .qualities .col { width: 155px; }
  .qualities .list > li { margin-bottom: 7px; }
  .qualities .sublist { margin-top: 2px; }
  .qualities .sublist > li { margin-bottom: 0; }
  .intro { position: absolute; left: 24px; width: 472px; top: 332px; }
  .page-tab {
    position: absolute; bottom: 0; left: 248px;
    width: 32px; height: 17px; background: var(--tab);
    font-size: 7px; text-align: center; line-height: 17px;
  }
  .forward { position: absolute; left: 24px; top: 64px; width: 230px; }
  .forward .list { margin-bottom: 6px; }
  .community { position: absolute; left: 266px; top: 248px; width: 234px; }
</style>
</head>
<body>

<section class="page page--left">
  <div class="photo photo--crucifix" role="img" aria-label="Carved wooden crucifix with risen Christ in white robes against a warm wood wall"></div>
  <h2 style="left:24px; top:305px;">The Rector We Seek</h2>
  <div class="intro">
    <p>In the past we have benefited from church leaders who nurtured our membership and guided us in the faith journeys we are each called to make. We seek a church leader who will uplift our parish and help us reach out to the greater community.</p>
    <p>The rector we prayerfully seek will lead by example and possess the following qualities:</p>
  </div>
  <div class="qualities">
    <ul class="list col">
      <li>Mature spiritual center
        <ul class="sublist">
          <li>Has a personal relationship with Christ that is integral to their being.</li>
          <li>Has a strong theological focus and a desire to seek and do God’s will.</li>
          <li>Holds a relevant interpretation of Christ’s teachings and an ability to convey it to those they encounter, both as a preacher and as a citizen in the broader community.</li>
          <li>Is grounded in the humility of Christ, knows who they are and are secure in that knowledge.</li>
        </ul>
      </li>
    </ul>
    <ul class="list col">
      <li>Effective communicator
        <ul class="sublist">
          <li>Delivers strong, thoughtful sermons that convey the Gospel as calls to action.</li>
          <li>Presents biblical perspectives in relevant ways, and within the context of our times.</li>
          <li>Is charismatic, authentic, honest and grounded in Christ’s teaching.</li>
          <li>Consistently lives their faith by being the hands and feet of Christ.</li>
        </ul>
      </li>
      <li>Courageous
        <ul class="sublist">
          <li>Is willing to do what is required for community outreach and congregational growth.</li>
          <li>Has the ability to operate outside their comfort zone.</li>
          <li>Is an attentive and discerning listener.</li>
          <li>Is open-minded and guided by Scripture.</li>
        </ul>
      </li>
    </ul>
    <ul class="list col">
      <li>Unconditionally caring
        <ul class="sublist">
          <li>A loving and caring rector who will guide St. Wendel toward its future.</li>
          <li>A rector who engages with those needing pastoral care.</li>
          <li>Brings a sense of joy and humor to their life and work.</li>
        </ul>
      </li>
      <li>Empowering
        <ul class="sublist">
          <li>St. Wendel has mature lay leadership that seeks an empowering leader to guide us.</li>
          <li>Continues to challenge others – and themselves – to grow in Christ.</li>
        </ul>
      </li>
      <li>Community minded
        <ul class="sublist">
          <li>Is a leader who has the interest and enthusiasm to be involved in the larger community</li>
        </ul>
      </li>
    </ul>
  </div>
  <div class="page-tab">pg 5</div>
</section>

<section class="page page--right">
  <h2 style="left:24px; top:27px;">Looking Forward</h2>
  <div class="forward">
    <p>St. Wendel is seeking a leader who will help us…</p>
    <ul class="list">
      <li>Nurture our church family and welcome others into it</li>
      <li>Provide opportunities for mutual ministry</li>
      <li>Build on our legacy as a spiritual center of our community</li>
      <li>Be an effective provider of community services for Paso Robles</li>
    </ul>
    <p>The rector we call will bring the talent, energy and enthusiasm we need to grow in the following areas:</p>
    <ul class="list">
      <li>Grow and diversify the membership of St. Wendel.</li>
      <li>Help us develop mentoring, tutoring and counseling programs; for example, programs that support children and the Hispanic community, raising awareness of St. Wendel as a resource for educational and spiritual development.</li>
      <li>Increase our support for area seniors, whom we have long served and wish to further serve.</li>
      <li>Use our fundraising events to involve more people from the greater Paso Robles community.</li>
      <li>Take a more active role and participation in community events celebrating milestones with which we are historically and culturally linked</li>
    </ul>
  </div>
  <div class="photo photo--doorway" role="img" aria-label="Parishioners gathering on the steps at the red door of the white church"></div>
  <div class="photo photo--congregation" role="img" aria-label="Smiling congregation singing in the pews of the sunlit church"></div>
  <h2 style="left:266px; top:222px;">Our Community</h2>
  <div class="community">
    <p>Cattle ranching. Hay farming. Vineyards. Aerospace manufacturing. Software development. Shopping. Good schools. We have it all – a rich history woven into a vibrant contemporary culture.</p>
    <p>Our city is El Paso de Robles (“Pass of the Oaks”), organized in 1889, overlooking the upper Salinas River, conveniently located midway between San Francisco and Los Angeles. Our community is a mix of local families that have been here for generations, retirees from urban centers north and south of the area, young families seeking a great community in which to raise their children, and immigrants seeking opportunities for a better life.</p>
    <p>City life revolves around a grand central park with an historic Hartwell library, a modern movie theater, award-winning restaurants and gathering places. Our city calendar is filled with family-friendly events, with both modern festivals and traditional celebrations that echo Paso’s pioneer roots.</p>
    <p>The San Luis Obispo-Paso Robles MSA (Metropolitan Statistical Area) ranked second most satisfied in the US on a recent Brightwell-Thrive Well Being Index. We also ranked 8 out of 189 metropolitan areas in overall well being.</p>
    <p>In recent years viticulture and winemaking has become more prominent,with Paso Robles being named “Wine Region of the Year” for 2013 by Vine Quarterly Magazine. The 270-plus wineries and a superior group of restaurants have led to a vibrant wine tourism industry. Paso Robles has been noted as a top vacation destination by the TravelNook and The Daily Ledger.</p>
    <p>For more information on the city of Paso Robles and surrounding communities, please visit our website at www.stwendelparish.org/rector.html</p>
  </div>
  <div class="page-tab">pg 6</div>
</section>

</body>
</html>
```